Thornfield Marsh, LLC Website

We are a small law firm in need of a website that contains the following:
1. Attractive main page
2. About us/attorney info for three people: Leonard Thornfield (attorney), Brent Marsh (attorney), and Melinda Carrow (legal assistant). We have bio's ready to submit.
3. Blog/video page. We'd like to post blogs and videos to help drive traffic
4. Multidistrict Litigation and Class Actions page, where we post information regarding active MDLs and Class actions that we are doing intake on.
Updates

Can you also please use the color "gold" in the design and logo? Thanks.

Industry/Entity Type

Legal

Coding

Coded - Design and coding required

Number of Pages Required

1 page

Colors
0054AA
0677BA
7BADD7
CADEEF
E8F1F8

Requirements
Must have
• 1. Attractive main page 2. About us/attorney info for three people: Leonard Thornfield (attorney), Brent Marsh (attorney), and Melinda Carrow (legal assistant). We have bio's ready to submit. 3. Blog/video page. We'd like to post blogs and videos to help drive traffic 4. Multidistrict Litigation and Class Actions page, where we post information regarding active MDLs and Class actions that we are doing intake on.

```html
<!DOCTYPE html>
<html lang="en">
<head>
<meta charset="utf-8">
<title>Thornfield Marsh, LLC — Lawyers</title>
<link rel="stylesheet" href="https://fonts.googleapis.com/css2?family=Cinzel:wght@500;600&family=Poppins:wght@400;500;600;700&display=swap">
<style>
:root{
  --navy:#0c1d86;
  --navy-deep:#09166b;
  --gold:#b9a066;
  --gold-light:#cdb77f;
  --ink:#1b1b1b;
  --muted:#5a5a5a;
  --paper:#ffffff;
  --panel:#eeeeee;
  --black:#000000;
}
*{box-sizing:border-box;margin:0;padding:0}
html,body{width:1200px;height:5021px;overflow:hidden;background:var(--paper)}
body{position:relative;font-family:"Poppins",sans-serif;color:var(--ink)}
.abs{position:absolute}
a{color:inherit;text-decoration:none}

/* header */
.site-header{position:absolute;left:0;top:0;width:1200px;height:123px;background:var(--paper)}
.brand{position:absolute;display:flex;align-items:center;gap:12px;border:3px solid var(--navy);padding:0 14px;height:53px}
.brand .mark{width:26px;height:26px;background:var(--navy)}
.brand .name{font-weight:600;font-size:19px;color:var(--gold);letter-spacing:.3px;white-space:nowrap}
.site-header .brand{left:74px;top:31px;width:296px}
.main-nav{position:absolute;left:544px;top:46px;display:flex;gap:34px;font-size:11px;font-weight:500;color:#222}
.main-nav .active{color:var(--navy);border-bottom:2px solid var(--gold);padding-bottom:4px}
.btn-contact-top{position:absolute;left:870px;top:34px;width:114px;height:36px;background:var(--navy);color:#fff;font-size:11px;font-weight:500;display:flex;align-items:center;justify-content:center}
.phone-top{position:absolute;left:1013px;top:32px;width:121px;height:38px;border:2px solid var(--navy);display:flex;align-items:center;justify-content:center;gap:6px;font-size:11px;font-weight:500;color:var(--navy)}
.phone-top .dot{width:18px;height:18px;border-radius:50%;background:var(--gold)}

/* hero */
.hero{position:absolute;left:0;top:123px;width:1200px;height:757px;background:linear-gradient(180deg,#3a2a1e 0%,#5a3b24 30%,#3b2616 55%,#0d0907 80%,#000 100%)}
.hero h1{position:absolute;left:0;top:510px;width:1200px;text-align:center;font-family:"Cinzel",serif;font-weight:500;font-size:50px;letter-spacing:2px;color:var(--gold)}
.hero p{position:absolute;left:300px;top:587px;width:600px;text-align:center;color:#fff;font-size:15px;line-height:24px}
.btn-gold{background:var(--gold);color:#fff;font-weight:500;display:flex;align-items:center;justify-content:center;letter-spacing:.5px}
.hero .btn-gold{position:absolute;left:502px;top:662px;width:195px;height:57px;font-size:18px}

/* about */
.about{position:absolute;left:72px;top:960px;width:1062px;height:579px;background:linear-gradient(120deg,#2a241f 0%,#6b625a 35%,#d9d6d1 70%,#f2f2f2 100%)}
.about-panel{position:absolute;left:542px;top:20px;width:500px;height:541px;background:rgba(238,238,238,.96);padding:80px 42px 0 42px}
.about-panel h2{font-size:46px;font-weight:700;color:var(--navy);line-height:1}
.eyebrow{font-size:17px;color:var(--gold);font-weight:500;display:flex;align-items:center;gap:12px}
.eyebrow .rule{width:48px;height:2px;background:var(--gold)}
.about-panel .eyebrow{margin-top:8px}
.about-panel p{font-size:12.6px;line-height:24px;color:#444;margin-top:22px;text-align:justify}
.about-panel .btn-gold{position:absolute;left:44px;top:452px;width:199px;height:59px;font-size:18px}

/* team */
.team{position:absolute;left:72px;top:1539px;width:1062px;height:574px;background:var(--black)}
.member{position:absolute;top:92px;width:344px;text-align:center}
.member svg{display:block;margin:0 auto}
.member .name{margin-top:6px;font-size:12.5px;font-weight:600;color:#fff;letter-spacing:.3px}
.member .role{font-size:10px;color:var(--gold);letter-spacing:.3px}
.team .more{position:absolute;left:520px;top:486px;color:#fff;font-size:18px}

/* why */
.why{position:absolute;left:72px;top:2207px;width:1062px;height:271px;border:7px solid var(--navy);background:#fff}
.why-head{position:absolute;left:-7px;top:-7px;width:260px;height:271px;background:var(--navy);padding:42px 0 0 32px}
.why-head h2{font-size:44px;line-height:58px;font-weight:700;color:#fff}
.why-head .rule{width:48px;height:2px;background:var(--gold);margin-top:18px}
.stat{position:absolute;top:56px}
.stat .num{font-size:42px;font-weight:700;color:var(--navy);line-height:1;margin-top:14px}
.stat .label{font-size:15px;color:#333;margin-top:8px}
.stat-divider{position:absolute;top:64px;width:1px;height:140px;background:#bbb}

/* services */
.services{position:absolute;left:0;top:2573px;width:1200px;height:887px;background:linear-gradient(135deg,#1c1a17 0%,#3e3a34 40%,#2a2722 70%,#14110e 100%)}
.svc-intro{position:absolute;left:64px;top:287px;width:392px;height:288px;text-align:center;color:#fff}
.svc-intro .frame-corner{position:absolute;width:90px;height:60px;border-color:#ccc;border-style:solid;border-width:0}
.svc-intro h2{margin-top:34px;font-size:44px;font-weight:600}
.svc-intro .eyebrow{justify-content:center;font-size:16px}
.svc-intro p{margin:26px auto 0;width:300px;font-size:12.5px;line-height:23px;text-align:justify;color:#ddd}
.svc-card{position:absolute;width:294px;height:318px;background:#fff;padding:30px 44px 0 44px}
.svc-card h3{margin-top:26px;font-size:25px;font-weight:600;color:var(--navy)}
.svc-card p{margin-top:14px;font-size:12.5px;line-height:21px;color:#555}
.svc-card .go{margin-top:18px;width:28px;height:28px;border-radius:50%;background:var(--gold);display:flex;align-items:center;justify-content:center}

/* solve */
.solve{position:absolute;left:0;top:3460px;width:1200px;height:596px;background:linear-gradient(90deg,#2a1a10 0%,#4a3020 30%,#241710 60%,#0f0a07 100%)}
.solve h2{position:absolute;left:520px;top:96px;width:630px;text-align:center;font-size:58px;line-height:72px;font-weight:600;color:#fff}
.solve p{position:absolute;left:590px;top:300px;width:490px;text-align:center;font-size:13px;line-height:21px;color:#eee}
.solve .btn-gold{position:absolute;left:627px;top:374px;width:380px;height:57px;font-size:18px}
.btn-outline{position:absolute;left:627px;top:446px;width:380px;height:57px;border:2px solid var(--gold);color:#fff;font-size:18px;font-weight:500;display:flex;align-items:center;justify-content:center}

/* blog */
.blog-head{position:absolute;left:0;top:4130px;width:1200px;text-align:center}
.blog-head h2{font-size:46px;font-weight:700;color:var(--navy);line-height:1}
.blog-head .eyebrow{justify-content:center;margin-top:10px;font-size:18px}
.post{position:absolute;top:4299px;width:290px;height:368px;background:#fff;box-shadow:0 2px 10px rgba(0,0,0,.12);border-bottom:4px solid var(--navy)}
.post .thumb{position:absolute;left:8px;top:8px;width:274px;height:187px}
.post .date{position:absolute;left:26px;top:222px;font-size:10px;color:#333;display:flex;align-items:center;gap:8px}
.post .date i{display:block;width:12px;height:12px;border:2px solid var(--gold)}
.post h3{position:absolute;left:26px;top:250px;font-size:16px;font-weight:500;color:var(--navy)}
.post p{position:absolute;left:26px;top:276px;width:238px;font-size:12.5px;line-height:20px;color:#444;text-align:justify}
.post .read{position:absolute;left:26px;top:330px;font-size:10px;font-weight:600;color:var(--navy);display:flex;align-items:center;gap:8px}
.post .read i{display:block;width:12px;height:12px;background:var(--gold)}
.pager{position:absolute;top:4725px;width:40px;height:40px;border-radius:50%;display:flex;align-items:center;justify-content:center}

/* footer */
.site-footer{position:absolute;left:0;top:4802px;width:1200px;height:219px;background:var(--navy)}
.site-footer .brand{left:68px;top:60px;width:294px;border-color:#fff}
.f-contact{position:absolute;top:64px;display:flex;gap:14px;color:#fff;font-size:13px;line-height:18px}
.f-contact .ico{width:28px;height:28px;border:1.5px solid #fff;flex:none;margin-top:6px}
.site-footer .rule{position:absolute;left:68px;top:138px;width:1066px;height:1px;background:rgba(255,255,255,.35)}
.copy{position:absolute;left:68px;top:167px;font-size:11px;color:#fff}
.socials{position:absolute;left:522px;top:156px;display:flex;gap:11px}
.socials span{width:31px;height:31px;border:1.5px solid #fff;display:block}
.f-nav{position:absolute;left:722px;top:167px;display:flex;gap:48px;font-size:11px;color:#fff}
</style>
</head>
<body>

<header class="site-header">
  <div class="brand"><span class="mark"></span><span class="name">THORNFIELD MARSH LLC</span></div>
  <nav class="main-nav">
    <a class="active">HOME</a><a>ABOUT US</a><a>SERVICES</a><a>BLOG</a>
  </nav>
  <a class="btn-contact-top">CONTACT US</a>
  <div class="phone-top"><span class="dot"></span>0145 678 210</div>
</header>

<section class="hero" role="img" aria-label="Wooden judge's gavel and brass scales on an open law book in a library">
  <h1>PROFESSIONAL LAW EXPERTISE</h1>
  <p>Lorem ipsum dolor sit amet, consectetur adipiscing elit, sed do eiusmod tempor incididunt ut labore et dolore magna aliqua</p>
  <a class="btn-gold">CONTACT US</a>
</section>

<section class="about" role="img" aria-label="Lawyer in a suit signing a document with a pen">
  <div class="about-panel">
    <h2>ABOUT US</h2>
    <div class="eyebrow">WHO WE ARE <span class="rule"></span></div>
    <p>Lorem ipsum dolor sit amet, consectetur adipiscing elit, sed do eiusmod tempor incididunt ut labore et dolore magna aliqua. Quis ipsum suspendisse ultrices gravida. Risus comm odo viverra maecenas accumsan lacus vel facilisis.</p>
    <p>Lorem ipsum dolor sit amet, consectetur adipiscing elit, sed do eiusmod tempor incididunt ut labore et dolore magna aliqua. Quis ipsum suspendisse ultrices gravida. Risus comm odo viverra maecenas accumsan lacus vel facilisis.</p>
    <a class="btn-gold">KNOW MORE</a>
  </div>
</section>

<section class="team">
  <div class="member" style="left:5px">
    <svg width="344" height="344" viewBox="0 0 344 344"><polygon points="172,0 344,172 172,344 0,172" fill="none" stroke="#b9a066" stroke-width="2"/><polygon points="172,12 332,172 172,332 12,172" fill="#7d8fa6" role="img" aria-label="Portrait of Leonard Thornfield"/></svg>
    <div class="name">LEONARD THORNFIELD</div><div class="role">ATTORNEY</div>
  </div>
  <div class="member" style="left:362px">
    <svg width="344" height="344" viewBox="0 0 344 344"><polygon points="172,0 344,172 172,344 0,172" fill="none" stroke="#b9a066" stroke-width="2"/><polygon points="172,12 332,172 172,332 12,172" fill="#a3121c" role="img" aria-label="Portrait of Brent Marsh holding a gavel"/></svg>
    <div class="name">BRENT MARSH</div><div class="role">ATTORNEY</div>
  </div>
  <div class="member" style="left:714px">
    <svg width="344" height="344" viewBox="0 0 344 344"><polygon points="172,0 344,172 172,344 0,172" fill="none" stroke="#b9a066" stroke-width="2"/><polygon points="172,12 332,172 172,332 12,172" fill="#cfd3d8" role="img" aria-label="Portrait of Melinda Carrow"/></svg>
    <div class="name">MELINDA CARROW</div><div class="role">LEGAL ASSISTANT</div>
  </div>
  <div class="more">→</div>
</section>

<section class="why">
  <div class="why-head"><h2>WHY<br>CHOOSE<br>US</h2><div class="rule"></div></div>
  <div class="stat" style="left:307px">
    <svg width="64" height="62" viewBox="0 0 64 62" fill="none" stroke="#b9a066" stroke-width="2"><path d="M8 30 L24 44 L40 44 L56 30"/><path d="M20 22 L32 30 L44 22"/><line x1="32" y1="4" x2="32" y2="18"/><line x1="16" y1="10" x2="48" y2="10"/></svg>
    <div class="num">200+</div><div class="label">Succesful Cases</div>
  </div>
  <div class="stat-divider" style="left:484px"></div>
  <div class="stat" style="left:505px">
    <svg width="64" height="62" viewBox="0 0 64 62" fill="none" stroke="#b9a066" stroke-width="2"><circle cx="32" cy="26" r="9"/><path d="M16 58 C16 42 48 42 48 58"/><path d="M22 8 L32 4 L42 8"/></svg>
    <div class="num">10+</div><div class="label">Expert Attorneys</div>
  </div>
  <div class="stat-divider" style="left:680px"></div>
  <div class="stat" style="left:702px">
    <svg width="64" height="62" viewBox="0 0 64 62" fill="none" stroke="#b9a066" stroke-width="2"><circle cx="20" cy="28" r="7"/><circle cx="44" cy="28" r="7"/><circle cx="32" cy="22" r="7"/><path d="M8 56 C8 42 56 42 56 56"/></svg>
    <div class="num">320+</div><div class="label">Happy Client</div>
  </div>
  <div class="stat-divider" style="left:846px"></div>
  <div class="stat" style="left:868px">
    <svg width="64" height="62" viewBox="0 0 64 62" fill="none" stroke="#b9a066" stroke-width="2"><circle cx="32" cy="22" r="16"/><path d="M22 36 L18 58 L32 50 L46 58 L42 36"/></svg>
    <div class="num">20+</div><div class="label">Award Winning</div>
  </div>
</section>

<section class="services" role="img" aria-label="Gavel resting on a desk beside legal papers">
  <div class="svc-intro">
    <span class="frame-corner" style="left:0;top:0;border-top-width:2px;border-left-width:2px"></span>
    <span class="frame-corner" style="right:0;top:0;border-top-width:2px;border-right-width:2px"></span>
    <span class="frame-corner" style="left:0;bottom:0;border-bottom-width:2px;border-left-width:2px"></span>
    <span class="frame-corner" style="right:0;bottom:0;border-bottom-width:2px;border-right-width:2px"></span>
    <h2>OUR SERVICES</h2>
    <div class="eyebrow"><span class="rule"></span>WHAT WE DO<span class="rule"></span></div>
    <p>Lorem ipsum dolor sit amet, consectetur adipiscing elit, sed do eiusmod tempor inc idid unt ut labore et dolore magna aliqua. Quis ipsum suspendisse ultrices gravida. Risus comm odo viverra maecenas</p>
  </div>
  <article class="svc-card" style="left:497px;top:107px">
    <svg width="60" height="60" viewBox="0 0 60 60" fill="none" stroke="#b9a066" stroke-width="2"><rect x="22" y="30" width="34" height="24"/><line x1="4" y1="26" x2="22" y2="8"/><rect x="14" y="4" width="14" height="8" transform="rotate(45 21 8)"/></svg>
    <h3>Business Law</h3>
    <p>Lorem ipsum dolor sit amet, consectetur adipiscing elit sed do eiusmod tempor</p>
    <div class="go"><svg width="14" height="10" viewBox="0 0 14 10" fill="none" stroke="#fff" stroke-width="2"><path d="M0 5H12M8 1L12 5L8 9"/></svg></div>
  </article>
  <article class="svc-card" style="left:824px;top:107px">
    <svg width="60" height="60" viewBox="0 0 60 60" fill="none" stroke="#b9a066" stroke-width="2"><circle cx="34" cy="18" r="7"/><path d="M22 56 V36 C22 28 46 28 46 36 V56"/><rect x="4" y="10" width="14" height="18"/></svg>
    <h3>Personal Injury</h3>
    <p>Lorem ipsum dolor sit amet, consectetur adipiscing elit sed do eiusmod tempor</p>
    <div class="go"><svg width="14" height="10" viewBox="0 0 14 10" fill="none" stroke="#fff" stroke-width="2"><path d="M0 5H12M8 1L12 5L8 9"/></svg></div>
  </article>
  <article class="svc-card" style="left:497px;top:452px">
    <svg width="60" height="60" viewBox="0 0 60 60" fill="none" stroke="#b9a066" stroke-width="2"><line x1="30" y1="6" x2="30" y2="52"/><line x1="10" y1="14" x2="50" y2="14"/><path d="M4 34 A8 8 0 0 0 20 34Z"/><path d="M40 34 A8 8 0 0 0 56 34Z"/><line x1="18" y1="54" x2="42" y2="54"/></svg>
    <h3>Criminal Law</h3>
    <p>Lorem ipsum dolor sit amet, consectetur adipiscing elit sed do eiusmod tempor</p>
    <div class="go"><svg width="14" height="10" viewBox="0 0 14 10" fill="none" stroke="#fff" stroke-width="2"><path d="M0 5H12M8 1L12 5L8 9"/></svg></div>
  </article>
  <article class="svc-card" style="left:824px;top:452px">
    <svg width="60" height="60" viewBox="0 0 60 60" fill="none" stroke="#b9a066" stroke-width="2"><rect x="8" y="6" width="34" height="46"/><line x1="14" y1="18" x2="36" y2="18"/><line x1="14" y1="26" x2="36" y2="26"/><circle cx="44" cy="42" r="10"/></svg>
    <h3>Corporate Law</h3>
    <p>Lorem ipsum dolor sit amet, consectetur adipiscing elit sed do eiusmod tempor</p>
    <div class="go"><svg width="14" height="10" viewBox="0 0 14 10" fill="none" stroke="#fff" stroke-width="2"><path d="M0 5H12M8 1L12 5L8 9"/></svg></div>
  </article>
</section>

<section class="solve" role="img" aria-label="Lawyer writing at a desk in a wood-panelled office">
  <h2>We Will Solve<br>Your Problem Today</h2>
  <p>Lorem ipsum dolor sit amet, consectetur adipiscing elit sed do eiusmod tempor incididunt ut labore et dolore magna aliqua. Quis ipsum suspen disse ultrices gravida.</p>
  <a class="btn-gold">MULTIDISTRICT LITIGATION</a>
  <a class="btn-outline">CLASS ACTIONS</a>
</section>

<section class="blog">
  <div class="blog-head">
    <h2>LATEST BLOG</h2>
    <div class="eyebrow"><span class="rule"></span>NEWS &amp; UPDATES<span class="rule"></span></div>
  </div>
  <article class="post" style="left:105px">
    <div class="thumb" role="img" aria-label="Two people in suits reviewing documents" style="background:linear-gradient(135deg,#2c2c2c,#8a8580)"></div>
    <div class="date"><i></i>JAN 20, 2025</div>
    <h3>Lorem ipsum dolor sit amet</h3>
    <p>Lorem ipsum dolor sit amet, consectetur adipisci elit, sed</p>
    <a class="read">READ MORE <i></i></a>
  </article>
  <article class="post" style="left:448px">
    <div class="thumb" role="img" aria-label="Hands passing a signed contract" style="background:linear-gradient(135deg,#a9c3c4,#e6e6e2)"></div>
    <div class="date"><i></i>FEB 26, 2025</div>
    <h3>Lorem ipsum dolor sit amet</h3>
    <p>Lorem ipsum dolor sit amet, consectetur adipisci elit, sed</p>
    <a class="read">READ MORE <i></i></a>
  </article>
  <article class="post" style="left:791px">
    <div class="thumb" role="img" aria-label="Lawyer explaining paperwork to a client" style="background:linear-gradient(135deg,#2c2c2c,#8a8580)"></div>
    <div class="date"><i></i>MARCH 20, 2024</div>
    <h3>Lorem ipsum dolor sit amet</h3>
    <p>Lorem ipsum dolor sit amet, consectetur adipisci elit, sed</p>
    <a class="read">READ MORE <i></i></a>
  </article>
  <div class="pager" style="left:549px;background:#fff;box-shadow:0 1px 6px rgba(0,0,0,.2)"><svg width="16" height="12" viewBox="0 0 16 12" fill="none" stroke="#b9a066" stroke-width="2"><path d="M16 6H2M6 1L1 6L6 11"/></svg></div>
  <div class="pager" style="left:607px;background:var(--gold)"><svg width="16" height="12" viewBox="0 0 16 12" fill="none" stroke="#fff" stroke-width="2"><path d="M0 6H14M10 1L15 6L10 11"/></svg></div>
</section>

<footer class="site-footer">
  <div class="brand"><span class="mark" style="background:#fff"></span><span class="name">THORNFIELD MARSH LLC</span></div>
  <div class="f-contact" style="left:448px"><span class="ico"></span><div>CALL US<br>8014 552 7390</div></div>
  <div class="f-contact" style="left:637px"><span class="ico"></span><div>EMAIL US<br>hello@thornfieldmarsh.law</div></div>
  <div class="f-contact" style="left:908px"><span class="ico"></span><div>Address line Dummy Here<br>Address line Here</div></div>
  <div class="rule"></div>
  <div class="copy">Copyright © 2025 &nbsp;All Rights Reserved By Company name</div>
  <div class="socials"><span></span><span></span><span></span><span></span></div>
  <nav class="f-nav"><a>HOME</a><a>ABOUT US</a><a>SERVICES</a><a>BLOG</a><a>CONTACT US</a></nav>
</footer>

</body>
</html>
```